Real Estate Brokerage - Sales Promo Flyer

We would like someone to design a 8x11 high gloss promotional flyer for our real estate agents to use in the field when presenting to a possible listing client (someone who wants to sell their home).

The flyer should include some of our brokerage's recent sales transaction numbers, as well as benefits to using our service.

We would like our design to have a professional appeal, with bold colors, and vivid images.

I have attached 5 images of recently sold homes:
247 Marisol Lane Trust, Palm Beach Gardens, Florida - Sold for $424,000
4718 Tierra Linda Ct, Boca Raton, FL 33431 - Sold for $415,000
418 Verbena Hills Drive, Palm Beach Gardens, Florida - Sold for $877,500
20417 Heron Bluff Circle, West Palm Beach, Florida - Sold for $380,000
382 Thistle Road, Greenacres, Florida - Sold for $234,500

I can provide any additional details you need. See attached files.
Updates

This flyer should contain our business name, logo, phone numbers, and website (however you see fit). PelicoHomes Palm Beach County | (561) 402-1186 Broward County | (954) 238-4417 www.pelicohomes-example.com

More Properties to Add: 418 Verbena Hills Drive, Palm Beach Gardens, Florida - Sold for $877,500 20417 Heron Bluff Circle, West Palm Beach, Florida - Sold for $380,000 382 Thistle Road, Greenacres, Florida - Sold for $234,500

I have added the Original Logo Images. Please use one of these in your design.

I have uploaded an image of our syndication partners, please add this to your flyers.

Please submit all of your Design. Thanks!

Please submit your edits

Industry/Entity Type

Real Estate

Requirements
Must have
• PelicoHomes is one word with a capital K and capital R.

Must have website and phone number.

PelicoHomes
www.pelicohomes-example.com
561-402-1186 - Palm Beach County
954-238-4417 - Broward County

```html
<!DOCTYPE html>
<html lang="en">
<head>
<meta charset="utf-8">
<title>PelicoHomes – Sold Flyer</title>
<link rel="stylesheet" href="https://fonts.googleapis.com/css2?family=Arimo:wght@400;700&family=Carlito:ital,wght@1,700&family=Lato:wght@300&display=swap">
<style>
  :root {
    --teal: #48c3d2;
    --ink: #1c1c1c;
    --body: #3a3a3a;
    --caption: #555555;
    --paper: #ffffff;
    --badge: #9a9a9a;
    --photo-a: #8fb585;
    --photo-b: #6f9c68;
  }
  * { box-sizing: border-box; margin: 0; padding: 0; }
  html, body { width: 1200px; height: 873px; overflow: hidden; background: var(--paper); }
  .flyer { position: relative; width: 1200px; height: 873px; background: var(--paper); font-family: "Arimo", Arial, sans-serif; color: var(--body); }
  .band { position: absolute; left: 0; width: 1200px; height: 30px; background: var(--teal); }
  .band--top { top: 0; }
  .band--bottom { bottom: 0; }

  .headline { position: absolute; top: 66px; left: 0; width: 1200px; text-align: center;
    font-family: "Lato", sans-serif; font-weight: 300; font-size: 80px; letter-spacing: 42px;
    color: var(--teal); line-height: 1; padding-left: 42px; }

  .listing { position: absolute; width: 173px; }
  .listing__photo { width: 173px; height: 134px; border: 3px solid var(--teal);
    background: linear-gradient(180deg, var(--photo-a), var(--photo-b)); }
  .listing__address { margin-top: 12px; font-size: 9.5px; line-height: 16px; letter-spacing: 0.6px; color: var(--caption); }
  .listing__price { font-family: "Carlito", sans-serif; font-style: italic; font-weight: 700; font-size: 16px; color: var(--ink); line-height: 20px; }

  .more { position: absolute; left: 440px; top: 376px; width: 160px; text-align: center;
    font-size: 30px; letter-spacing: 14px; line-height: 46px; color: var(--teal); }

  .brand { position: absolute; left: 61px; top: 592px; display: flex; align-items: center; gap: 12px; }
  .brand__mark { width: 58px; height: 50px; }
  .brand__name { font-weight: 700; font-size: 22px; letter-spacing: 5px; color: var(--ink); }
  .contact { position: absolute; left: 61px; top: 652px; }
  .contact__web { font-size: 15px; letter-spacing: 4.3px; color: var(--ink); line-height: 20px; }
  .contact__phone { font-size: 12.5px; letter-spacing: 1px; color: var(--ink); line-height: 22px; }

  .badges { position: absolute; left: 61px; top: 728px; display: flex; align-items: flex-end; gap: 8px; }
  .badge { background: var(--badge); }
  .badge--square { width: 37px; height: 38px; }
  .badge--partner { height: 14px; border-radius: 2px; margin-bottom: 10px; }

  .pitch { position: absolute; left: 625px; top: 173px; width: 520px; text-align: center; }
  .pitch__lead, .pitch__para { font-size: 12.5px; letter-spacing: 0.8px; line-height: 22px; color: var(--body); }
  .pitch__para { margin-top: 22px; }
  .pitch__heading { font-family: "Carlito", sans-serif; font-style: italic; font-weight: 700; font-size: 17px; color: var(--ink); line-height: 22px; margin-top: 20px; }
  .facts { list-style: none; }
  .facts li { font-family: "Carlito", sans-serif; font-style: italic; font-weight: 700; font-size: 17.5px; line-height: 22px; color: var(--teal); }
  .facts li::before { content: "•"; font-style: normal; font-size: 13px; margin-right: 18px; }
  .pitch__heading--where { margin-top: 21px; }
</style>
</head>
<body>
<main class="flyer">
  <div class="band band--top"></div>

  <h1 class="headline">SOLD!</h1>

  <article class="listing" style="left:61px;top:173px">
    <div class="listing__photo" role="img" aria-label="Photo of a sold single-storey home with palm trees and lawn, marked sold"></div>
    <p class="listing__address">247 Marisol Lane Trust,<br>Palm Beach Gardens, Florida</p>
    <p class="listing__price">$424,000</p>
  </article>
  <article class="listing" style="left:247px;top:173px">
    <div class="listing__photo" role="img" aria-label="Photo of a sold two-storey Mediterranean home with palms, marked sold"></div>
    <p class="listing__address">418 Verbena Hills Drive,<br>Palm Beach Gardens, Florida</p>
    <p class="listing__price">$877,500</p>
  </article>
  <article class="listing" style="left:433px;top:173px">
    <div class="listing__photo" role="img" aria-label="Photo of a sold tile-roof home with garage and garden, marked sold"></div>
    <p class="listing__address">382 Thistle Road,<br>Greenacres, Florida</p>
    <p class="listing__price">$234,500</p>
  </article>
  <article class="listing" style="left:61px;top:378px">
    <div class="listing__photo" role="img" aria-label="Photo of a sold home behind a large shade tree, marked sold"></div>
    <p class="listing__address">4718 Tierra Linda Ct,<br>Boca Raton, FL 33431</p>
    <p class="listing__price">$415,000</p>
  </article>
  <article class="listing" style="left:247px;top:378px">
    <div class="listing__photo" role="img" aria-label="Photo of a sold ranch home with driveway and lawn, marked sold"></div>
    <p class="listing__address">20417 Heron Bluff Circle,<br>West Palm Beach, Florida</p>
    <p class="listing__price">$380,000</p>
  </article>

  <p class="more">And many more!</p>

  <div class="brand">
    <svg class="brand__mark" viewBox="0 0 58 50" aria-hidden="true"><circle cx="29" cy="25" r="24" fill="var(--teal)"/></svg>
    <span class="brand__name">PelicoHomes</span>
  </div>

  <div class="contact">
    <p class="contact__web">www.pelicohomes-example.com</p>
    <p class="contact__phone">561-402-1186 - Palm Beach County</p>
    <p class="contact__phone">954-238-4417 - Broward County</p>
  </div>

  <div class="badges" aria-label="Membership and listing partner badges">
    <span class="badge badge--square"></span>
    <span class="badge badge--square"></span>
    <span class="badge badge--partner" style="width:62px"></span>
    <span class="badge badge--partner" style="width:50px"></span>
    <span class="badge badge--partner" style="width:58px"></span>
    <span class="badge badge--partner" style="width:44px"></span>
    <span class="badge badge--partner" style="width:66px"></span>
  </div>

  <section class="pitch">
    <p class="pitch__lead">Inventory is at an all time Low and Prices are going way up!<br>Qualified buyers are waiting for great homes like yours.<br>PelicoHomes is Selling Homes for Top Dollar.</p>

    <h2 class="pitch__heading">The Facts</h2>
    <ul class="facts">
      <li>64 sales year to date</li>
      <li>15 sales over 200k</li>
      <li>8 sales over 300k</li>
      <li>Sale of the Year $877.5k</li>
    </ul>

    <h2 class="pitch__heading pitch__heading--where">Where We List Your Home</h2>
    <ul class="facts">
      <li>Multiple Listing Service (MLS)</li>
      <li>30+ Real Estate Websites (Homefindr, Nestly, HouseLift, Searchly, Portalview Real Estate, Roomspot)</li>
      <li>30+ Social Media Websites (Friendwall, Chirpline, Circlenet, Pinboardly)</li>
    </ul>

    <p class="pitch__para">By listing your home with PelicoHomes, you will receive maximum exposure, more offers, and ultimately will sell your home faster than listing with a traditional real estate brokerage.</p>
    <p class="pitch__para">Our proven marketing system drives a greater volume of traffic to your listing than any of our competitors.</p>
    <p class="pitch__para">PelicoHomes is recognized as a real estate leader in both Palm Beach and Broward County. Our knowledgable agents and aggressive marketing will make sure that you get the best price for your home, in the least amount of time.</p>
  </section>

  <div class="band band--bottom"></div>
</main>
</body>
</html>
```